Label for Glass Cleaning Bottle

Our New Zealand-based company designs and sells glass cabinets and display cases. 75% of our customers are other businesses who want to display products in their shop or showroom. The other 25% of our customers are householders who want a glass cabinet for their personal collectables. We have been trading 2 years now, and are expanding rapidly.
One thing we really want to do for our customers is provide them with a complimentary bottle of glass cleaner when they purchase a glass cabinet from us. It is a gesture of goodwill, but also will make their experience of owning one of our cabinets more satisfying because clean glass is important with glass cabinets. We have developed our own glass cleaning formula, and now need to put it in bottles to be given away. All we need now is an appropriate label on the bottle that is both recognisable as a glass cleaner and reinforces the image of our company as professional.
The label will be professionally offset-printed with an overseal, and applied to the bottle by hand.
We would like the final output to be in Adobe Indesign, or compatible file format.
The shape of the bottle is conical. The label's APPROXIMATE measurements will be 70mm high, 265mm wide at the bottom and 135mm at the bottom. A similar bottle can be seen on this webpage: http://www.velmorkparts.co.nz/online-store/products/Trigger-Spray-Bottle-500ml.aspx?pid=481207#Description

Reason: Recent submissions have been of a high standard, so I want to provide enough time for this trend to continue.

Target Market(s)

The target market will be people who purchase our glass cabinets, most of whom are retailers of some sort but some of whom are householders.

Industry/Entity Type

It Company

Requirements
Must have
• "Glass Cleaner"
"Optimised to achieve grease-free sparkling glass"
Plinthwell Furnishing logo
Company web address: www.plinthwellfurnishing.co.nz
"To reorder, email: glasscleaner@plinthwellfurnishing.co.nz"
"Non-toxic, Streak-free, No ammonia"
[Corporate colour is green, as per logo. Secondary colours are orange, purple and grey.]
[Please use New Zealand (British) spelling]
Nice to have
• Please view our website and brochure on the Resources page for the look and feel of our company. In particular we like our logo, so it is possible you can take a lead from this. The logo emblem is designed to be evocative of glass.
The label can be 5 colour. A spot colour will probably be used for the logo itself. The spot colour is 41,0,70,10.

```html
<!DOCTYPE html>
<html lang="en-NZ">
<head>
<meta charset="utf-8">
<title>Glass Cleaner Label – Plinthwell Furnishing</title>
<link rel="stylesheet" href="https://fonts.googleapis.com/css2?family=Dancing+Script:wght@500&family=Raleway:wght@300;400;600&display=swap">
<style>
  :root {
    --paper: #ffffff;
    --taupe: #8a7967;
    --leaf: #8dc63f;
    --leaf-soft: #8fb86f;
    --leaf-text: #8dc63f;
    --slate: #939393;
    --ink-light: #ffffff;
  }
  html, body {
    margin: 0;
    padding: 0;
    overflow: hidden;
    background: var(--paper);
  }
  .canvas {
    position: relative;
    width: 1200px;
    height: 1200px;
    background: var(--paper);
    overflow: hidden;
    font-family: "Raleway", sans-serif;
  }
  .band {
    position: absolute;
    left: 0;
    width: 1200px;
  }
  .band--top-rule { top: 322px; height: 38px; background: var(--taupe); }
  .band--brand { top: 360px; height: 157px; background: var(--paper); }
  .band--title { top: 517px; height: 348px; background: var(--leaf); }
  .band--claims { top: 865px; height: 157px; background: var(--slate); }
  .band--bottom-rule { top: 1022px; height: 26px; background: var(--taupe); }

  .brand-mark {
    position: absolute;
    left: 28px;
    top: 403px;
    height: 70px;
    display: flex;
    align-items: center;
    gap: 20px;
  }
  .brand-mark__square {
    width: 70px;
    height: 70px;
    background: var(--leaf-soft);
    opacity: 0.55;
  }
  .brand-mark__name {
    font-weight: 600;
    font-size: 36px;
    letter-spacing: 1px;
    color: var(--leaf-soft);
    line-height: 1;
  }

  .contact {
    position: absolute;
    right: 25px;
    top: 420px;
    text-align: right;
    color: var(--leaf-text);
    font-weight: 300;
  }
  .contact__web {
    font-size: 36px;
    line-height: 1.1;
    letter-spacing: -0.5px;
  }
  .contact__reorder {
    font-size: 20px;
    margin-top: 6px;
  }

  .product-title {
    position: absolute;
    left: 0;
    top: 575px;
    width: 1275px;
    text-align: center;
    font-family: "Dancing Script", cursive;
    font-weight: 500;
    font-size: 190px;
    line-height: 1.2;
    color: var(--ink-light);
    margin: 0;
  }

  .claims {
    position: absolute;
    left: 0;
    top: 902px;
    width: 1210px;
    text-align: center;
    color: var(--ink-light);
    font-weight: 300;
    font-size: 38px;
    line-height: 57px;
    margin: 0;
  }
</style>
</head>
<body>
<main class="canvas">
  <div class="band band--top-rule"></div>
  <div class="band band--brand"></div>
  <div class="band band--title"></div>
  <div class="band band--claims"></div>
  <div class="band band--bottom-rule"></div>

  <div class="brand-mark">
    <div class="brand-mark__square"></div>
    <div class="brand-mark__name">PLINTHWELL FURNISHING</div>
  </div>

  <div class="contact">
    <div class="contact__web">www.plinthwellfurnishing.co.nz</div>
    <div class="contact__reorder">To reorder, email: glasscleaner@plinthwellfurnishing.co.nz</div>
  </div>

  <h1 class="product-title">Glass Cleaner</h1>

  <p class="claims">
    Optimised to achieve grease-free sparkling glass<br>
    Non-toxic, Streak-free, No ammonia
  </p>
</main>
</body>
</html>
```